Qvo Brightforge Website

All the descriptions are available in the attached file. The designer has to structure the website and find the right images and icons. The website should look modern and avoid using images of real humans rather use animated images. Please note that the design should include home page, all the 4 services page , the contact us would be at the bottom of home page.

```html
<!DOCTYPE html>
<html lang="en">
<head>
<meta charset="utf-8">
<title>Qvo Brightforge</title>
<link href="https://fonts.googleapis.com/css2?family=Orbitron:wght@700&family=Roboto:wght@400;500;700&display=swap" rel="stylesheet">
<style>
:root{
  --navy:#0b1f3c;
  --blue:#0a74da;
  --orange:#f7941d;
  --green:#4cc20a;
  --white:#ffffff;
  --text:#2c2c2c;
  --field:#f1f2f4;
}
*{margin:0;padding:0;box-sizing:border-box}
html,body{width:1200px;height:3317px;overflow:hidden}
body{position:relative;font-family:"Roboto",sans-serif;color:var(--text);background:var(--white)}
.abs{position:absolute}
.art{position:absolute;border-radius:4px}
/* header + hero */
.hero{position:absolute;left:0;top:0;width:1200px;height:514px;background:var(--navy)}
.brand{position:absolute;display:flex;align-items:center;gap:8px;font-family:"Roboto",sans-serif;font-weight:700;color:var(--white)}
.brand .dot{width:12px;height:12px;background:var(--orange)}
.nav{position:absolute;display:flex;gap:22px;font-size:14px;color:var(--white)}
.nav .active{color:var(--orange)}
.quote-btn{position:absolute;left:961px;top:16px;width:128px;height:46px;border-radius:23px;background:var(--blue);color:var(--white);font-weight:700;font-size:15px;display:flex;align-items:center;justify-content:center}
.rule{position:absolute;left:112px;top:84px;width:977px;height:1px;background:#2a3d5c}
.hero h1{position:absolute;left:112px;top:184px;width:500px;font-size:31px;line-height:44px;font-weight:700;color:var(--white);letter-spacing:.5px}
.hero p{position:absolute;left:112px;top:337px;font-size:17.5px;font-weight:500;color:var(--white)}
/* section marks */
.mark{position:absolute;width:36px;height:36px;left:582px}
.mark i{position:absolute;width:14px;height:14px}
.mark i:first-child{left:0;top:0;background:var(--green)}
.mark i:last-child{left:17px;top:17px;width:19px;height:19px;background:var(--orange)}
.display{position:absolute;left:0;width:1200px;text-align:center;font-family:"Orbitron",sans-serif;font-weight:700;font-size:36px;letter-spacing:1px}
/* welcome */
.welcome-text{position:absolute;left:590px;top:718px;width:498px;font-size:15px;line-height:28.3px;text-align:justify;color:#333}
.welcome-text p+p{margin-top:13px}
.learn-btn{position:absolute;left:590px;top:1030px;width:129px;height:46px;border-radius:23px;background:var(--navy);color:var(--white);font-weight:700;font-size:15px;display:flex;align-items:center;justify-content:center}
/* services */
.services-bg{position:absolute;left:0;top:1123px;width:1200px;height:1491px}
.service h3{position:absolute;font-size:30px;font-weight:500;color:var(--white);letter-spacing:.5px}
.service p{position:absolute;font-size:15px;line-height:28.3px;color:var(--white);text-align:justify}
.service svg{position:absolute}
/* contact */
.contact-title{position:absolute;left:112px;top:2812px;font-size:21px;font-weight:500;color:#222}
.contact-row{position:absolute;left:112px;display:flex;gap:20px;align-items:flex-start;font-size:16.5px;line-height:30px;color:#222;z-index:1}
.contact-row svg{flex:none;margin-top:2px}
.tile{position:absolute}
.card{position:absolute;z-index:5;left:627px;top:2790px;width:461px;height:354px;background:var(--white);border-radius:6px;box-shadow:0 4px 18px rgba(0,0,0,.12)}
.card h4{position:absolute;left:0;top:26px;width:100%;text-align:center;font-size:21px;font-weight:500;color:#222}
.field{position:absolute;background:var(--field);font-size:13.5px;color:#777;padding:14px 22px}
.submit{position:absolute;left:33px;top:274px;width:395px;height:47px;border-radius:24px;background:var(--blue);color:var(--white);font-weight:700;font-size:15px;display:flex;align-items:center;justify-content:center}
/* footer */
.footer{position:absolute;z-index:0;left:0;top:3094px;width:1200px;height:223px;background:var(--navy)}
.footer-nav{position:absolute;right:111px;top:123px;display:flex;gap:33px;font-size:14.5px;color:var(--white)}
.copy{position:absolute;right:111px;top:159px;font-size:14.5px;color:var(--white)}
</style>
</head>
<body>

<header class="hero">
  <div class="brand" style="left:112px;top:28px;font-size:20px"><span class="dot"></span>Qvo Brightforge</div>
  <nav class="nav" style="left:589px;top:31px">
    <span class="active">Home</span><span>Services</span><span>Products</span><span>Blog</span><span>Contact us</span>
  </nav>
  <div class="quote-btn">Get a quote</div>
  <div class="rule"></div>
  <h1>EMPOWER YOUR DIGITAL JOURNEY WITH OUR ADVANCED IT SOLUTIONS.</h1>
  <p>From data to web and mobile apps, we've got you covered.</p>
  <svg class="abs" style="left:112px;top:393px" width="20" height="30" viewBox="0 0 20 30" fill="none" stroke="#fff" stroke-width="1.6">
    <rect x="1" y="1" width="18" height="28" rx="9"/><path d="M10 7v12M6 15l4 4 4-4"/>
  </svg>
  <div class="art" role="img" aria-label="Illustration of a laptop with analytics dashboards and charts" style="left:622px;top:126px;width:485px;height:337px;background:linear-gradient(135deg,#f7941d 0%,#e9eef5 35%,#d6e3f3 70%,#0a74da 100%)"></div>
</header>

<section class="welcome">
  <div class="mark" style="top:561px"><i></i><i></i></div>
  <h2 class="display" style="top:606px;color:var(--blue)">WELCOME TO QVO BRIGHTFORGE</h2>
  <div class="art" role="img" aria-label="Illustration of two colleagues working together at a desk with a monitor" style="left:113px;top:716px;width:415px;height:337px;background:linear-gradient(160deg,#dff3c9 0%,#e6effa 55%,#c9ddf3 100%)"></div>
  <div class="welcome-text">
    <p>We are a forward-thinking IT consulting firm specializing in providing cutting-edge data analytics, web application development, and mobile app development services. Our passion for innovation and technology drives us to deliver tailor-made solutions that empower businesses to thrive in the digital landscape.</p>
    <p>We take pride in our ability to collaborate with early-stage startups as their technology partner, helping them navigate the challenges of launching and scaling their ventures. Our team of experienced professionals works closely with clients, understanding their unique requirements and goals, to craft bespoke solutions that propel growth and foster success.</p>
  </div>
  <div class="learn-btn">Learn More</div>
</section>

<section class="services">
  <svg class="services-bg" viewBox="0 1123 1200 1491" width="1200" height="1491">
    <rect x="0" y="1123" width="1200" height="1491" fill="#0a74da"/>
    <polygon points="0,1671 1200,1558 1200,2176 0,2289" fill="#0b1f3c"/>
  </svg>
  <div class="mark" style="top:1179px"><i></i><i></i></div>
  <h2 class="display" style="top:1224px;color:var(--white)">OUR SERVICES</h2>

  <div class="service">
    <h3 style="left:111px;top:1337px">DATA ANALYTICS</h3>
    <p style="left:111px;top:1388px;width:458px;text-align:left">At Qvo Brightforge, our proficiency consists of linking your leadership team's objectives with the relevant data that holds significance. We recognize the importance of not only delivering precise and dependable data but also presenting it in a format that is easily comprehensible and aligned with your business goals.</p>
    <svg style="left:111px;top:1546px" width="24" height="16" viewBox="0 0 24 16" fill="none" stroke="#fff" stroke-width="2"><path d="M1 8h21M15 1l7 7-7 7"/></svg>
    <div class="art" role="img" aria-label="Illustration of two analysts examining a dashboard on a large monitor with a magnifier" style="left:716px;top:1279px;width:351px;height:289px;background:linear-gradient(135deg,#f7941d 0%,#e7eef8 40%,#3b8fe0 100%)"></div>
  </div>

  <div class="service">
    <div class="art" role="img" aria-label="Illustration of a web page layout on a desktop monitor with interface elements" style="left:113px;top:1684px;width:363px;height:245px;background:linear-gradient(135deg,#4cc20a 0%,#4a6cf0 50%,#1fb4e6 100%)"></div>
    <h3 style="left:632px;top:1717px">WEB DEVELOPMENT</h3>
    <p style="left:632px;top:1769px;width:458px">At Qvo Brightforge, we are a trailblazing web development company committed to delivering cutting-edge digital solutions that empower businesses to excel in the ever-evolving online landscape.</p>
    <svg style="left:632px;top:1880px" width="24" height="16" viewBox="0 0 24 16" fill="none" stroke="#fff" stroke-width="2"><path d="M1 8h21M15 1l7 7-7 7"/></svg>
  </div>

  <div class="service">
    <h3 style="left:112px;top:2017px">MOBILE APP DEVELOPMENT</h3>
    <p style="left:112px;top:2069px;width:460px">At Qvo Brightforge, we are a pioneering mobile app development company dedicated to crafting exceptional digital experiences that captivate and engage users across various platforms.</p>
    <svg style="left:112px;top:2181px" width="24" height="16" viewBox="0 0 24 16" fill="none" stroke="#fff" stroke-width="2"><path d="M1 8h21M15 1l7 7-7 7"/></svg>
    <div class="art" role="img" aria-label="Illustration of two people beside a large smartphone showing an app form" style="left:721px;top:1912px;width:367px;height:322px;background:linear-gradient(135deg,#f7941d 0%,#2d3a52 40%,#1aa3e8 100%)"></div>
  </div>

  <div class="service">
    <div class="art" role="img" aria-label="Illustration of a light bulb launching from a laptop with two celebrating founders" style="left:113px;top:2286px;width:366px;height:305px;background:linear-gradient(135deg,#4cc20a 0%,#8fb4f3 45%,#f7941d 100%)"></div>
    <h3 style="left:632px;top:2333px">START-UP TECH PARTNER</h3>
    <p style="left:632px;top:2386px;width:458px">At Qvo Brightforge, we are committed to supporting early-stage start-ups on their journey to success by providing comprehensive technical partner services.</p>
    <svg style="left:632px;top:2496px" width="24" height="16" viewBox="0 0 24 16" fill="none" stroke="#fff" stroke-width="2"><path d="M1 8h21M15 1l7 7-7 7"/></svg>
  </div>
</section>

<footer class="footer">
  <div class="brand" style="left:113px;top:70px;font-size:30px"><span class="dot" style="width:16px;height:16px"></span>Qvo Brightforge</div>
  <nav class="footer-nav"><span>Home</span><span>Services</span><span>Products</span><span>Blog</span><span>Contact us</span></nav>
  <div class="copy">2023 Qvo Brightforge. All Rights Reserved.</div>
</footer>

<section class="contact">
  <div class="mark" style="top:2661px"><i></i><i></i></div>
  <h2 class="display" style="top:2707px;color:var(--blue)">GET IN TOUCH</h2>
  <div class="tile" style="left:418px;top:2804px;width:124px;height:123px;background:#fdecd2"></div>
  <div class="tile" style="left:317px;top:2940px;width:156px;height:154px;background:#d6e5f7"></div>
  <div class="tile" style="left:489px;top:2943px;width:124px;height:125px;background:#dcf4d0"></div>
  <div class="contact-title">Contact Us</div>
  <div class="contact-row" style="top:2868px">
    <svg width="30" height="32" viewBox="0 0 24 24"><path fill="#111" d="M12 2a7 7 0 0 0-7 7c0 5 7 13 7 13s7-8 7-13a7 7 0 0 0-7-7zm0 9.5A2.5 2.5 0 1 1 12 6.5a2.5 2.5 0 0 1 0 5z"/></svg>
    <span>Suite 12/40 Larkmoor Avenue,<br>Fernvale WA 6001</span>
  </div>
  <div class="contact-row" style="top:2944px">
    <svg width="30" height="30" viewBox="0 0 24 24"><path fill="#111" d="M6.6 10.8a15 15 0 0 0 6.6 6.6l2.2-2.2c.3-.3.7-.4 1-.2 1.1.4 2.3.6 3.6.6.6 0 1 .4 1 1V20c0 .6-.4 1-1 1A17 17 0 0 1 3 4c0-.6.4-1 1-1h3.5c.6 0 1 .4 1 1 0 1.3.2 2.5.6 3.6.1.3 0 .7-.2 1z"/></svg>
    <span>+61 (08) 5550 0142 (Sales / Support)</span>
  </div>
  <div class="contact-row" style="top:3002px">
    <svg width="30" height="30" viewBox="0 0 24 24"><path fill="#111" d="M2 5h20v14H2zm2 2v.5l8 5 8-5V7l-8 5z"/></svg>
    <span>hello@qvobrightforge.example</span>
  </div>

  <form class="card">
    <h4>Book An Appointment</h4>
    <div class="field" style="left:30px;top:67px;width:199px;height:46px">Name</div>
    <div class="field" style="left:233px;top:67px;width:198px;height:46px">Phone</div>
    <div class="field" style="left:30px;top:119px;width:401px;height:46px">Email</div>
    <div class="field" style="left:30px;top:170px;width:401px;height:92px">Message</div>
    <div class="submit">Submit now</div>
  </form>
</section>

</body>
</html>
```